Marketing material for IT Company
Brochure/Sales Sheet/Flyer
Brochure will be in two languages, and tri-fold. Would go like this; front (outer) side: first fold: page for information in 2nd languge, second fold: page for information in 2nd language, third fold: cover page in 1st language; back side (inner) side: first fold is for information in 1st language, second fold is for information in 1st language, third fold is cover page for 2nd language.
Information Technology
Brochure view and dimensions are in an uploaded file. Size of flyer equals to size of 1 fold of brochure (i.e one brochure size = 3 flyers size). Size of Sales Sheet is equal to brochure's size. (Sales Sheet won't be folded).
Trifold Brochure view and dimensions
Tulmori logo and Divisions logos (CMYK)
Tulmori logo and Divisions logos (PMS)
Tulmori vertical logo and Divisions vertical logos (CMYK)
Tulmori vertical logo and Divisions vertical logos (PMS)
Tulmori old Brochure (uploaded as an example)
Example of our folder, if it can help
Example of our biz card, if it can help
To help you understand how we see our brochure, one more PIC
Tulmori logo colors information

```html
<!DOCTYPE html>
<html lang="en">
<head>
<meta charset="utf-8">
<title>Tulmori Flyers and Tri-fold Brochure</title>
<link href="https://fonts.googleapis.com/css2?family=Open+Sans:wght@400;600;700&display=swap" rel="stylesheet">
<style>
  :root{
    --bg:#e9e6e1;
    --paper:#ffffff;
    --ink:#4a4a4a;
    --ink-soft:#8a8a8a;
    --brand:#3b3b3b;
    --green:#6cb33f;
    --blue:#2a8fd0;
    --orange:#f39c12;
    --red:#e2413a;
    --yellow:#f6c21b;
    --purple:#8e5aa8;
    --photo-office:linear-gradient(160deg,#dfe6ec 0%,#b9c6d2 55%,#8796a6 100%);
    --photo-blue:linear-gradient(160deg,#dce8f3 0%,#9fb8d0 60%,#6a87a5 100%);
    --photo-tech:linear-gradient(160deg,#8fa6bd 0%,#4f6a86 55%,#2c3e55 100%);
    --photo-warm:linear-gradient(160deg,#e7ddd0 0%,#c2ad93 60%,#8d7760 100%);
  }
  *{box-sizing:border-box;margin:0;padding:0}
  html,body{width:1200px;height:780px;overflow:hidden;background:var(--bg)}
  body{position:relative;font-family:"Open Sans",Arial,sans-serif;color:var(--ink)}

  .sheet{position:absolute;background:var(--paper);box-shadow:0 2px 6px rgba(0,0,0,.18);overflow:hidden}

  /* flyer */
  .flyer{width:139px;height:341px;display:flex;flex-direction:column}
  .brand{display:flex;align-items:center;gap:5px;height:34px;padding:0 10px;font-weight:700;font-size:14px;color:var(--brand);letter-spacing:-.2px}
  .brand-dot{width:13px;height:13px;border-radius:50%;background:var(--orange);flex:none}
  .photo{width:100%}
  .flyer .photo{height:112px}
  .division{display:flex;align-items:center;gap:4px;padding:9px 10px 5px;font-size:8px;font-weight:600;color:var(--brand)}
  .division-mark{width:9px;height:9px;border-radius:50%;flex:none}
  .body-copy{font-size:4.6px;line-height:1.45;color:var(--ink-soft);padding:0 10px}
  .points{list-style:none;padding:5px 10px 0;font-size:4.6px;line-height:1.5;color:var(--ink)}
  .points li{display:flex;align-items:center;gap:3px}
  .points li::before{content:"";width:3px;height:3px;border-radius:50%;background:var(--blue);flex:none}
  .stripe{height:4px;background:linear-gradient(90deg,var(--green) 0 20%,var(--blue) 20% 40%,var(--purple) 40% 60%,var(--red) 60% 80%,var(--orange) 80% 100%)}
  .flyer .stripe{margin-top:auto}
  .url{height:14px;display:flex;align-items:center;justify-content:center;font-size:5px;color:var(--ink-soft);letter-spacing:.5px}

  /* brochure */
  .brochure{width:473px;height:341px}
  .panel{position:absolute;top:0;width:157.7px;height:100%}
  .panel-left{left:0}
  .panel-mid{left:157.7px;border-left:1px solid #eee}
  .panel-right{left:315.4px;border-left:1px solid #eee}
  .panel .body-copy{padding:0 10px}
  .panel-top{padding-top:12px}
  .panel-top .body-copy+.body-copy{margin-top:4px}
  .photo-band{position:absolute;left:0;top:108px;width:315.4px;height:80px;display:flex}
  .photo-band .photo{height:100%;width:50%}
  .panel-bottom{position:absolute;left:0;top:192px;width:100%}
  .brochure-foot{position:absolute;left:0;bottom:0;width:315.4px}
  .cover-brand{position:absolute;top:70px;left:0;width:100%;display:flex;flex-direction:column;align-items:center;gap:8px;font-weight:700;font-size:20px;color:var(--brand)}
  .cover-dot{width:44px;height:44px;border-radius:50%;background:var(--orange)}
  .cover-photo{position:absolute;left:0;bottom:0;width:100%;height:160px}
</style>
</head>
<body>

<!-- top row -->
<article class="sheet flyer" style="left:89px;top:31px">
  <header class="brand"><span class="brand-dot"></span>tulmori</header>
  <div class="photo" style="background:var(--photo-office)" role="img" aria-label="Photo of business team in an office"></div>
  <div class="division"><span class="division-mark" style="background:var(--green)"></span>Tulmori solutions</div>
  <p class="body-copy">We deliver reliable IT services that help your business grow, stay secure and work smarter every day.</p>
  <ul class="points"><li>Network design and setup</li><li>Managed servers and storage</li><li>Round the clock support</li></ul>
  <div class="stripe"></div>
  <footer class="url">www.lorvex.net</footer>
</article>

<article class="sheet flyer" style="left:233px;top:31px">
  <header class="brand"><span class="brand-dot"></span>tulmori</header>
  <div class="photo" style="background:var(--photo-office)" role="img" aria-label="Photo of business team in an office"></div>
  <div class="division"><span class="division-mark" style="background:var(--green)"></span>Tulmori solutions</div>
  <p class="body-copy">We deliver reliable IT services that help your business grow, stay secure and work smarter every day.</p>
  <ul class="points"><li>Network design and setup</li><li>Managed servers and storage</li><li>Round the clock support</li></ul>
  <div class="stripe"></div>
  <footer class="url">www.lorvex.net</footer>
</article>

<article class="sheet flyer" style="left:379px;top:31px">
  <header class="brand"><span class="brand-dot"></span>tulmori</header>
  <div class="photo" style="background:var(--photo-blue)" role="img" aria-label="Photo of businessman at a desk"></div>
  <div class="division"><span class="division-mark" style="background:var(--blue)"></span>Tulmori systems</div>
  <p class="body-copy">We deliver reliable IT services that help your business grow, stay secure and work smarter every day.</p>
  <ul class="points"><li>Network design and setup</li><li>Managed servers and storage</li><li>Round the clock support</li></ul>
  <div class="stripe"></div>
  <footer class="url">www.lorvex.net</footer>
</article>

<article class="sheet flyer" style="left:526px;top:31px">
  <header class="brand"><span class="brand-dot"></span>tulmori</header>
  <div class="photo" style="background:var(--photo-blue)" role="img" aria-label="Photo of businessman at a desk"></div>
  <div class="division"><span class="division-mark" style="background:var(--blue)"></span>Tulmori systems</div>
  <p class="body-copy">We deliver reliable IT services that help your business grow, stay secure and work smarter every day.</p>
  <ul class="points"><li>Network design and setup</li><li>Managed servers and storage</li><li>Round the clock support</li></ul>
  <div class="stripe"></div>
  <footer class="url">www.lorvex.net</footer>
</article>

<section class="sheet brochure" style="left:696px;top:31px">
  <div class="panel panel-left">
    <div class="panel-top">
      <p class="body-copy">We deliver reliable IT services that help your business grow, stay secure and work smarter every day.</p>
      <p class="body-copy">We deliver reliable IT services that help your business grow, stay secure and work smarter every day.</p>
      <ul class="points"><li>Network design and setup</li><li>Managed servers and storage</li><li>Round the clock support</li></ul>
    </div>
    <div class="panel-bottom">
      <div class="division"><span class="division-mark" style="background:var(--orange)"></span>Tulmori support</div>
    </div>
  </div>
  <div class="panel panel-mid">
    <div class="panel-top">
      <p class="body-copy">We deliver reliable IT services that help your business grow, stay secure and work smarter every day.</p>
    </div>
    <div class="panel-bottom">
      <div class="division"><span class="division-mark" style="background:var(--green)"></span>Tulmori solutions</div>
      <ul class="points"><li>Network design and setup</li><li>Managed servers and storage</li><li>Round the clock support</li></ul>
    </div>
  </div>
  <div class="photo-band">
    <div class="photo" style="background:var(--photo-warm)" role="img" aria-label="Photo of modern office building interior"></div>
    <div class="photo" style="background:var(--photo-office)" role="img" aria-label="Photo of smiling businessman"></div>
  </div>
  <div class="brochure-foot"><div class="stripe"></div><div class="url">www.lorvex.net</div></div>
  <div class="panel panel-right">
    <div class="cover-brand"><span class="cover-dot"></span>tulmori</div>
    <div class="cover-photo" style="background:var(--photo-tech)" role="img" aria-label="Photo of a hand touching a digital interface"></div>
  </div>
</section>

<!-- bottom row -->
<article class="sheet flyer" style="left:89px;top:403px">
  <header class="brand"><span class="brand-dot"></span>tulmori</header>
  <div class="photo" style="background:var(--photo-blue)" role="img" aria-label="Photo of businessmen shaking hands"></div>
  <div class="division"><span class="division-mark" style="background:var(--red)"></span>Tulmori cloud</div>
  <p class="body-copy">We deliver reliable IT services that help your business grow, stay secure and work smarter every day.</p>
  <ul class="points"><li>Network design and setup</li><li>Managed servers and storage</li><li>Round the clock support</li></ul>
  <div class="stripe"></div>
  <footer class="url">www.lorvex.net</footer>
</article>

<article class="sheet flyer" style="left:233px;top:403px">
  <header class="brand"><span class="brand-dot"></span>tulmori</header>
  <div class="photo" style="background:var(--photo-blue)" role="img" aria-label="Photo of businessmen shaking hands"></div>
  <div class="division"><span class="division-mark" style="background:var(--red)"></span>Tulmori cloud</div>
  <p class="body-copy">We deliver reliable IT services that help your business grow, stay secure and work smarter every day.</p>
  <ul class="points"><li>Network design and setup</li><li>Managed servers and storage</li><li>Round the clock support</li></ul>
  <div class="stripe"></div>
  <footer class="url">www.lorvex.net</footer>
</article>

<article class="sheet flyer" style="left:379px;top:403px">
  <header class="brand"><span class="brand-dot"></span>tulmori</header>
  <div class="photo" style="background:var(--photo-office)" role="img" aria-label="Photo of support team with headsets"></div>
  <div class="division"><span class="division-mark" style="background:var(--yellow)"></span>Tulmori support</div>
  <p class="body-copy">We deliver reliable IT services that help your business grow, stay secure and work smarter every day.</p>
  <ul class="points"><li>Network design and setup</li><li>Managed servers and storage</li><li>Round the clock support</li></ul>
  <div class="stripe"></div>
  <footer class="url">www.lorvex.net</footer>
</article>

<article class="sheet flyer" style="left:526px;top:403px">
  <header class="brand"><span class="brand-dot"></span>tulmori</header>
  <div class="photo" style="background:var(--photo-office)" role="img" aria-label="Photo of support team with headsets"></div>
  <div class="division"><span class="division-mark" style="background:var(--yellow)"></span>Tulmori support</div>
  <p class="body-copy">We deliver reliable IT services that help your business grow, stay secure and work smarter every day.</p>
  <ul class="points"><li>Network design and setup</li><li>Managed servers and storage</li><li>Round the clock support</li></ul>
  <div class="stripe"></div>
  <footer class="url">www.lorvex.net</footer>
</article>

<section class="sheet brochure" style="left:696px;top:403px">
  <div class="panel panel-left">
    <div class="panel-top">
      <p class="body-copy">We deliver reliable IT services that help your business grow, stay secure and work smarter every day.</p>
      <p class="body-copy">We deliver reliable IT services that help your business grow, stay secure and work smarter every day.</p>
      <ul class="points"><li>Network design and setup</li><li>Managed servers and storage</li><li>Round the clock support</li></ul>
    </div>
    <div class="panel-bottom">
      <div class="division"><span class="division-mark" style="background:var(--orange)"></span>Tulmori support</div>
    </div>
  </div>
  <div class="panel panel-mid">
    <div class="panel-top">
      <p class="body-copy">We deliver reliable IT services that help your business grow, stay secure and work smarter every day.</p>
    </div>
    <div class="panel-bottom">
      <div class="division"><span class="division-mark" style="background:var(--green)"></span>Tulmori solutions</div>
      <ul class="points"><li>Network design and setup</li><li>Managed servers and storage</li><li>Round the clock support</li></ul>
    </div>
  </div>
  <div class="photo-band">
    <div class="photo" style="background:var(--photo-warm)" role="img" aria-label="Photo of modern office building interior"></div>
    <div class="photo" style="background:var(--photo-office)" role="img" aria-label="Photo of smiling businessman"></div>
  </div>
  <div class="brochure-foot"><div class="stripe"></div><div class="url">www.lorvex.net</div></div>
  <div class="panel panel-right">
    <div class="cover-brand"><span class="cover-dot"></span>tulmori</div>
    <div class="cover-photo" style="background:var(--photo-tech)" role="img" aria-label="Photo of a hand touching a digital interface"></div>
  </div>
</section>

</body>
</html>
```